2-Page Flyer for the Information Session about the Quiet Venture Pathway

This is a flyer to announce/advertise an evening Information Session about the Quiet Venture Pathway. This Program aims at mindfully rethinking and redesigning work (and life) for people who feel stuck or not entirely satisfied with their work and/or life (please see draft flyer attached for more details). This Program is property of Bright Meadow, a company that uses a combination of Mindfulness, Design, and Entrepreneurship to help people achieve greater happiness (in their work and lives).
Updates

Target Market(s)

People who feel stuck or not entirely satisfied with their work and/or life (please see draft flyer attached for more details)

Font styles to use
Serif
Sans Serif

Colors
ffffff
f37122
33a6d7
acd037

Requirements
Must have
• All of what I will say below is suggestive (I’m not a design expert), and I’m open to divert from it, if it makes sense and feels more interesting.
• I thought initially of a 2-page flyer (please see draft flyer attached). The first page could help people grasp the essence of the event quickly (in 1 or 2 minutes), and then, if they are interested/motivated, they would continue reading through page 2, which has more info about the Program in itself.
• Potential Structure
• Page 1
• . About the Information Session on the Quiet Venture Pathway
• . Visible Date & Time, Contacts, Venue (and other relevant info)
• . About me (the facilitator)
• Page 2
• . About the Quiet Venture Pathway
• I include a Powerpoint draft of the flyer with the content. The design is rudimentary and precarious from an aesthetics/organization point of view, and this is mainly where I need help (and maybe in other aspects too!).
• On the flyer, I would like to include:
• . A photo of myself (I attach 1 picture).
• . 1 or 2 beautiful-nature photos (cropped or full). One may have to do with looking at the sky, dreaming, and imagining a new work and life (2 photos with sky and clouds attached). The other has to do with walking the transformation journey (the photo with the person walking through the forest path).
• . bright meadow logo or logos (there are two slightly different ones, that can be used for different purposes). For the first page, I would like the bright meadow logo that has "bright meadow" written on the bottom, with the saying "Calm, Craft and Enterprise for Joyful Living" beneath. This is the main logo. For the 2nd page, you can choose the logo that adapts better.
• - Where it says the "the way out is in" it would be great to have a similar font to the one I attach (see file "Font_the_way_out_is_in.png" and Torvenscript-qr.ttf
Nice to have
• In terms of colours, I would not divert much from the logo colours (and of course white and black). I would like the flyer to be quite white. Almost like fairy-tale white: the white horse, the white snow, the white of the stars, the white heaven. White could be the base colour. White means peace, tranquillity, calm contentment, a smile.
• And then use the other colours. The green of the mindfulness. The blue of the sky, the dreams. And the orange of the sun, the energy, the fire, the action. And maybe the black for text.
• Where it says the "the way out is in" it would be great to have a similar font to the one I attach (see file "Font_the_way_out_is_in".
• I would like this flyer to be a piece of art, in every possible way. Simple, beautiful, ease, light, peaceful, calm happy. Just like the Quiet Venture Pathway and bright meadow Company that I am creating intends to be. The mission of this Program and Company is to be a designer, a painter (a Picasso) of happier and more fulfilling human lives.
• I am very much looking forward to seeing your proposal(s).

```html
<!DOCTYPE html>
<html lang="en">
<head>
<meta charset="utf-8">
<title>Quiet Venture Pathway – Information Session Flyer</title>
<link href="https://fonts.googleapis.com/css2?family=Oswald:wght@500;600;700&family=Open+Sans:wght@400;600;700&family=Dancing+Script:wght@600&display=swap" rel="stylesheet">
<style>
:root{
  --orange:#f37122;
  --blue:#33a6d7;
  --green:#acd037;
  --ink:#222;
  --charcoal:#3a3a3d;
  --grey-bg:#8a8a8a;
  --white:#fff;
}
*{box-sizing:border-box;margin:0;padding:0}
html,body{width:1200px;height:1200px;overflow:hidden;background:var(--grey-bg)}
body{position:relative;font-family:'Open Sans',sans-serif;color:var(--ink)}
.page{position:absolute;top:222px;width:566px;height:732px;background:linear-gradient(#fff,#f3f3f3);overflow:hidden}
.page--front{left:26px}
.page--back{left:605px;background:#fff}
.abs{position:absolute}
.cond{font-family:'Oswald',sans-serif}

/* front */
.hero-block{left:39px;top:0;width:217px;height:303px;background:var(--orange)}
.hero-photo{left:18px;top:12px;width:190px;height:291px;background:linear-gradient(160deg,#4b6a8e,#2f4560 70%,#2a3a4e);border-radius:90px 90px 0 0}
.brand{left:286px;top:12px;width:230px;text-align:center}
.brand-row{display:flex;align-items:center;justify-content:center;gap:10px}
.brand-dot{width:50px;height:50px;border-radius:50%;background:var(--blue)}
.brand-name{font-size:27px;line-height:1;color:var(--blue);font-weight:400;text-align:left}
.brand-tag{font-size:7.4px;font-weight:700;margin-top:14px}
.headline-box{left:183px;top:107px;width:378px;height:170px;background:var(--charcoal);text-align:center;padding-top:22px}
.headline-kicker{font-size:19px;color:var(--green);font-weight:600;line-height:1}
.headline-main{font-size:56px;color:var(--orange);font-weight:600;line-height:1.1;letter-spacing:-1px}
.headline-sub{font-size:19px;color:var(--blue);font-weight:600;font-family:'Open Sans',sans-serif;margin-top:8px;letter-spacing:.3px}
.event{left:0;width:566px;text-align:center}
.event-title{top:312px;font-size:35px;font-weight:700;letter-spacing:.2px;line-height:1.1}
.event-date{top:353px;font-size:18px;color:var(--blue);font-weight:700;line-height:23px}
.event-venue{top:400px;font-size:15px;font-weight:600;line-height:18px}
.event-copy{top:420px;font-size:10.3px;line-height:14px;padding:0 20px}
.event-who{top:462px;font-size:10.3px;line-height:14px;padding:0 22px}
.event-who b{display:block;font-weight:600}
.facilitator-photo{left:26px;top:530px;width:148px;height:202px;background:linear-gradient(#eceff2,#c9cfd6)}
.facilitator{left:188px;top:532px;width:362px}
.facilitator-head{font-size:8.8px;font-weight:700;white-space:nowrap}
.facilitator-head span{font-family:'Oswald',sans-serif;color:var(--green);font-size:11.5px;font-weight:600}
.facilitator-bio{font-size:7.2px;line-height:10.2px;margin-top:4px;text-align:justify}
.facilitator-link{font-size:10px;font-weight:700;margin-top:5px;white-space:nowrap}
.facilitator-link span{color:var(--blue);font-size:11.5px}
.booking-bar{left:174px;top:687px;width:392px;height:37px;background:var(--charcoal)}
.booking-tab{left:174px;top:687px;width:128px;height:37px;background:var(--orange);clip-path:polygon(0 0,100% 0,88% 100%,0 100%);color:#fff;font-size:12px;font-weight:700;line-height:14px;text-align:center;padding-top:4px}
.booking-details{left:302px;top:692px;width:264px;text-align:center;color:#fff;font-size:7.6px;font-weight:700;line-height:11px}

/* back */
.intro{left:0;top:0;width:566px;height:138px;background:linear-gradient(#c06f33,#d8843f 60%,#e59a55);color:#fff;padding:16px 18px}
.intro-title{font-size:35px;font-weight:700;line-height:1}
.intro-copy{font-size:12px;font-weight:600;line-height:15.5px;margin-top:9px}
.section-head{font-family:'Oswald',sans-serif;font-size:19px;font-weight:600;line-height:1}
.program{left:18px;top:148px;width:267px}
.program .section-head{color:var(--blue)}
.program p{font-size:11.2px;line-height:15px;text-align:justify;hyphens:auto;margin-top:4px}
.cycle{left:318px;top:146px;width:240px;height:190px}
.why{left:18px;top:332px;width:252px}
.why .section-head{color:var(--orange)}
.how{left:301px;top:332px;width:251px}
.how .section-head{color:var(--green)}
.col-copy{font-size:9.4px;line-height:12.2px;margin-top:5px}
.col-copy b{font-weight:700}
.ticks{list-style:none;font-size:9.4px;line-height:12.2px}
.ticks li{margin-top:3px}
.ticks svg{width:10px;height:9px;margin-right:4px;vertical-align:-1px}
.forest{left:0;top:544px;width:566px;height:136px;background:linear-gradient(90deg,#2a2015,#4a3826 40%,#8a6a3a 52%,#4a3826 64%,#1f1a12)}
.quote{left:164px;top:582px;color:#fff}
.quote-text{font-family:'Dancing Script',cursive;font-size:34px;line-height:1}
.quote-by{font-size:11px;color:var(--orange);margin-left:110px;margin-top:2px}
.mini-brand{left:464px;top:638px;display:flex;align-items:center;gap:5px}
.mini-brand .brand-dot{width:24px;height:24px}
.mini-brand .brand-name{font-size:11px;color:var(--blue)}
.footer{left:0;top:680px;width:566px;height:52px;background:var(--orange);color:#fff;display:flex;align-items:center;padding-left:18px;font-weight:700}
.footer-label{font-size:12px;margin-right:16px}
.footer-phone{font-size:9.8px;padding-right:10px;border-right:1px solid #fff;line-height:30px}
.footer-mail{font-size:9.8px;padding-left:8px}
</style>
</head>
<body>

<section class="page page--front">
  <div class="abs hero-block"></div>
  <div class="abs hero-photo" role="img" aria-label="Portrait photo of the facilitator giving a thumbs up"></div>

  <div class="abs brand">
    <div class="brand-row"><span class="brand-dot"></span><span class="brand-name">bright<br>meadow</span></div>
    <p class="brand-tag">Calm, Craft and Enterprise for Joyful Living</p>
  </div>

  <div class="abs headline-box cond">
    <p class="headline-kicker">Mindfulness, Design and Entrepreneurship</p>
    <p class="headline-main">FOR HAPPINESS</p>
    <p class="headline-sub">FREE INFORMATION SESSION</p>
  </div>

  <h1 class="abs event event-title cond">QUIET VENTURE PATHWAY</h1>
  <p class="abs event event-date">THURSDAY 5TH SEPTEMBER 2019<br>19:30 TO 21:00</p>
  <p class="abs event event-venue">VENUE: TIDEWELL COWORKING, C/ ALMENDRO 42, BARCELONA</p>
  <p class="abs event event-copy">The purpose of this free Information Session is to give you a real insight into the Quiet Venture Pathway and how it can help you make the most of your professional and personal life.</p>
  <p class="abs event event-who"><b>WHO CAN COME</b>Whether you come on your own, or with friends or family, you'll be warmly welcomed. The session will take place on Thursday the 5th September 2019, from 19:30 to 21:00, at Tidewell Coworking. Please see information below to get in contact or to book a seat.</p>

  <div class="abs facilitator-photo" role="img" aria-label="Portrait photo of the facilitator wearing a scarf"></div>
  <div class="abs facilitator">
    <p class="facilitator-head"><span>FACILITATOR:</span> Dr Marco Lindqvist, Visiting Research Fellow, Harrowfield University</p>
    <p class="facilitator-bio">Marco joined the Harrowfield University School of Management as a Lecturer in Entrepreneurship in 2015. He completed his PhD in Entrepreneurship at Kelmont Business School in 2014, receiving the prestigious Academy of Enterprise Studies' Calloway Doctoral Dissertation Award. He began his business career as a Production Engineer for Veltrix, and later as a Sales Engineer for Norvane. After his MBA, he served as a Strategy Consultant for Oriel Business School. Originally from Portugal, Marco enjoys designing and launching new ideas, international communities, mindfulness retreats, and musical improvisation. He nurtures a close connection to Stillwater Mindfulness Centre, where he has practiced and volunteered over 9 months. He has a broad experience of sharing the benefits of mindfulness with others.</p>
    <p class="facilitator-link">More about the facilitator: <span>www.brightmeadow.example/marco</span></p>
  </div>

  <div class="abs booking-bar"></div>
  <div class="abs booking-tab">Information &amp;<br>Booking</div>
  <p class="abs booking-details">+34 600 000 123 (call and message)<br>Email: info@brightmeadow.example</p>
</section>

<section class="page page--back">
  <header class="abs intro">
    <h2 class="intro-title cond">WHAT IS QUIET VENTURE PATHWAY</h2>
    <p class="intro-copy">Being mindful means being aware and awake. Entrepreneurship is the creation of a new form of organising. Mindful Entrepreneurship is then the process of creating or redesigning your work and life with awareness, in a way that is reflective of you, of your passions and values, thus conducing to a greater sense of fulfilment and happiness.</p>
  </header>

  <div class="abs program">
    <h3 class="section-head">THE PROGRAM</h3>
    <p>The Quiet Venture Pathway is a 4-month long transformative journey designed for people who feel stuck or not entirely satisfied with their professional and/or personal life. It will be of benefit for everyone, at any stage. The Program entails a five-hour workshop each month, complemented by two-hour weekly peer support meetings. It combines mindfulness techniques, design thinking methodology, and entrepreneurship frameworks.</p>
  </div>

  <svg class="abs cycle" viewBox="0 0 240 190" font-family="Open Sans, sans-serif" text-anchor="middle">
    <g fill="#fff">
      <circle cx="104" cy="36" r="33" fill="#8dc63f"/>
      <circle cx="176" cy="93" r="33" fill="#4a90c2"/>
      <circle cx="104" cy="152" r="33" fill="#e8792f"/>
      <circle cx="39" cy="93" r="33" fill="#c6c6c6"/>
      <g font-size="6.5"><text x="104" y="30">Workshop 1</text><text x="176" y="87">Workshop 2</text><text x="104" y="146">Workshop 3</text><text x="39" y="87">Workshop 4</text></g>
      <g font-size="8.5" font-weight="600"><text x="104" y="40">INSIGHT</text><text x="176" y="97">DESIGN</text><text x="104" y="156">EXECUTE</text><text x="39" y="97">PRESENT</text></g>
      <g font-size="6" font-style="italic"><text x="104" y="49">(5 hours)</text><text x="176" y="106">(5 hours)</text><text x="104" y="165">(5 hours)</text><text x="39" y="106">(5 hours)</text></g>
    </g>
    <g fill="none" stroke-width="2.5">
      <path d="M140 62 l10 10 m0 -8 v8 h-8" stroke="#8dc63f"/>
      <path d="M150 128 l-10 10 m0 -8 v8 h8" stroke="#4a90c2"/>
      <path d="M74 134 l-10 -10 m0 8 v-8 h8" stroke="#e8792f"/>
      <path d="M62 62 l10 -10 m-8 0 h8 v8" stroke="#c6c6c6"/>
    </g>
    <g fill="#9a9a9a" font-size="6.5" font-style="italic">
      <text x="30" y="45">WPS meetings</text>
      <text x="207" y="30">Weekly Peer Support</text><text x="207" y="38">(WPS) meetings</text><text x="207" y="46">(2 hours)</text>
      <text x="207" y="150">WPS meetings</text>
      <text x="30" y="150">WPS meetings</text>
    </g>
  </svg>

  <div class="abs why">
    <h3 class="section-head">WHY</h3>
    <p class="col-copy"><b>Many people are not satisfied with their work or life, but they don't know what to do about it. This Program offers you a safe place to conduct your inner journey with collective support, helping you to reflect, design and do something about it.<br>It aims at:</b></p>
    <ul class="ticks">
      <li><svg viewBox="0 0 10 9"><path d="M1 5 l3 3 l5 -7" fill="none" stroke="#8dc63f" stroke-width="2"/></svg>Increasing awareness, clarity and confidence</li>
      <li><svg viewBox="0 0 10 9"><path d="M1 5 l3 3 l5 -7" fill="none" stroke="#8dc63f" stroke-width="2"/></svg>Having a deeper insight on what makes you happier and what you want</li>
      <li><svg viewBox="0 0 10 9"><path d="M1 5 l3 3 l5 -7" fill="none" stroke="#8dc63f" stroke-width="2"/></svg>Developing a clear design integrating your intended work and life</li>
      <li><svg viewBox="0 0 10 9"><path d="M1 5 l3 3 l5 -7" fill="none" stroke="#8dc63f" stroke-width="2"/></svg>Start executing this design.</li>
    </ul>
  </div>

  <div class="abs how">
    <h3 class="section-head">HOW</h3>
    <p class="col-copy"><b>This Program differs from existing entrepreneurial programs in many ways:</b></p>
    <ul class="ticks">
      <li><svg viewBox="0 0 10 9"><path d="M1 5 l3 3 l5 -7" fill="none" stroke="#f37122" stroke-width="2"/></svg>Uses mindfulness and self analysis to look deeply into yourself</li>
      <li><svg viewBox="0 0 10 9"><path d="M1 5 l3 3 l5 -7" fill="none" stroke="#f37122" stroke-width="2"/></svg>Design and execution decisions are based on happiness rather than only financials</li>
      <li><svg viewBox="0 0 10 9"><path d="M1 5 l3 3 l5 -7" fill="none" stroke="#f37122" stroke-width="2"/></svg>Holistic and inclusive design process, integrating work and life, and building synergies between your different parts.</li>
    </ul>
    <p class="col-copy" style="margin-top:2px"><b>The Program's format includes lectures, individual work, group sharing, guided activities, experiential exercises, video, audio, handouts and other resources</b></p>
  </div>

  <div class="abs forest" role="img" aria-label="Photo of a person walking along a sunlit forest path between tall trees"></div>
  <div class="abs quote">
    <p class="quote-text">The way out is in</p>
    <p class="quote-by">Zen Master Anan Vell</p>
  </div>
  <div class="abs mini-brand"><span class="brand-dot"></span><span class="brand-name">bright<br>meadow</span></div>

  <footer class="abs footer">
    <span class="footer-label">Information &amp; Booking</span>
    <span class="footer-phone">+34 600 000 123 (call and message)</span>
    <span class="footer-mail">Email: info@brightmeadow.example</span>
  </footer>
</section>

</body>
</html>
```